Homepage design for female-owned English/French speaking Law firm

Brief Update - we prefer not to have a photo of a person in the hero shot

Corvell.com.au is the website for a English/French Bilingual Female-owned Law Firm, Morillaqua Corvell.
Overall Design notes:
Professional, yet warm and welcoming
Historic foundations but Progressive, woman-owned, sleek, innovative and modern.
Approachable, casual yet professional. Sans-serif font and light colours would help this
2 languages switched by flags (English/French)

Winner must provide
Home page design
Standard (inner) page design (can be provided after winner is selected)
All photos used in the design without charge
Updates

Requirements
Should not have
• Update - we prefer not to have a photo of a person in the hero shot

```html
<!DOCTYPE html>
<html lang="en">
<head>
<meta charset="utf-8">
<title>Morillaqua Corvell — Solicitors</title>
<link rel="stylesheet" href="https://fonts.googleapis.com/css2?family=Roboto:wght@300;400;500;700;900&display=swap">
<style>
:root{
  --orange:#f5a06e;
  --teal:#1aa3ab;
  --sky:#bfe3f6;
  --ink:#222;
  --line:#dcdcdc;
  --white:#fff;
}
*{box-sizing:border-box;margin:0;padding:0}
html,body{width:1200px;height:4243px;overflow:hidden}
body{font-family:'Roboto',sans-serif;color:var(--ink);background:var(--white);position:relative}
section,header,footer{position:relative;width:1200px;overflow:hidden}
.abs{position:absolute}
.btn{position:absolute;display:flex;align-items:center;justify-content:center;background:var(--orange);color:#fff;font-size:14px;font-weight:500}
.brand{display:flex;align-items:center;gap:10px;font-family:'Roboto',sans-serif;font-weight:500;color:var(--orange);font-size:24px;white-space:nowrap}
.brand-mark{width:14px;height:14px;background:var(--orange);display:block}

/* header */
.site-header{height:90px;background:#fff}
.nav{position:absolute;top:0;left:446px;display:flex;height:90px;align-items:center;font-size:15px;color:#555}
.nav a{display:flex;align-items:center;height:90px;padding:0 16px;text-decoration:none;color:#555}
.nav a.active{background:var(--teal);color:#fff}
.lang{position:absolute;left:967px;top:25px;width:122px;height:42px;border:1px solid var(--line);display:flex;align-items:center;gap:8px;padding-left:12px;font-size:14px;color:var(--orange)}
.flag{width:26px;height:16px;background:linear-gradient(#c33 0 14%,#fff 14% 28%,#c33 28% 42%,#fff 42% 57%,#c33 57% 71%,#fff 71% 85%,#c33 85%);position:relative}
.flag::before{content:"";position:absolute;left:0;top:0;width:11px;height:9px;background:#2b4a8c}

/* hero */
.hero{height:585px;background:linear-gradient(100deg,#f7d9cb 0%,#f6c8ae 55%,#f3b894 100%)}
.hero-portrait{position:absolute;left:590px;top:0;width:500px;height:585px;background:linear-gradient(180deg,#f3c4a6,#e9ddd3 55%,#cfd5d8)}
.hero-desk{position:absolute;left:0;top:470px;width:600px;height:115px;background:linear-gradient(180deg,rgba(190,210,220,.5),rgba(160,190,205,.7))}
.hero-text{position:absolute;left:90px;top:135px;width:490px;text-align:center}
.hero-text .pre{font-size:24px;color:#333}
.hero-text h1{font-size:66px;font-weight:900;letter-spacing:-1px;line-height:1.15;color:#111}
.hero-text .sub{font-size:32px;font-weight:300;color:#222;margin-top:2px}
.hero-text p{font-size:16px;color:#333;line-height:1.8;margin-top:16px}
.dots{position:absolute;display:flex;gap:5px}
.dots i{width:12px;height:12px;border-radius:50%;border:1.5px solid #fff;display:block}
.dots i.on{background:var(--teal);border-color:var(--teal)}
.quick{position:absolute;left:750px;top:501px;width:338px;height:84px;background:var(--orange);color:#fff;font-size:33px;font-weight:700;display:flex;align-items:center;justify-content:center}

/* welcome */
.welcome{height:477px}
.welcome .pre{position:absolute;left:111px;top:67px;font-size:21px}
.welcome h2{position:absolute;left:111px;top:90px;font-size:50px;color:var(--orange);font-weight:700}
.welcome .copy{position:absolute;left:111px;top:160px;width:580px;font-size:14px;line-height:1.55;color:#555}
.outline-btn{position:absolute;left:111px;top:363px;width:236px;height:43px;border:1.5px solid var(--orange);color:var(--orange);font-size:14px;display:flex;align-items:center;justify-content:center;letter-spacing:.5px}
.enquiry-note{position:absolute;left:750px;top:18px;width:338px;text-align:center;font-size:14px;line-height:1.5;color:#444}
.field{position:absolute;left:773px;width:294px;height:46px;border:1px solid var(--line);font-size:12px;color:#aaa;padding:15px 16px;display:flex;justify-content:space-between}
.field svg{width:14px;height:14px;stroke:#aaa;fill:none;stroke-width:1.5}
.appt{position:absolute;left:750px;top:360px;width:338px;height:46px;background:var(--teal);color:#fff;font-size:13px;font-weight:500;display:flex;align-items:center;justify-content:space-between;padding:0 24px}

/* practice */
.practice{height:798px;background:linear-gradient(180deg,#c2e5f8,#aedbf2)}
.scale-deco{position:absolute;left:280px;top:80px;width:720px;height:700px;background:radial-gradient(ellipse at 60% 55%,rgba(120,160,190,.25),rgba(120,160,190,0) 65%)}
.sec-pre{position:absolute;left:0;width:1200px;text-align:center;font-size:20px;color:#333}
.sec-title{position:absolute;left:0;width:1200px;text-align:center;font-size:50px;font-weight:700;color:var(--orange)}
.area{position:absolute;width:254px;height:267px;text-align:center;padding-top:22px}
.area.featured{background:#fff;box-shadow:0 2px 12px rgba(0,0,0,.08)}
.area svg.icon{width:44px;height:44px;stroke:#444;fill:none;stroke-width:1.6}
.area.featured svg.icon{stroke:var(--orange)}
.area h3{font-size:18px;font-weight:500;color:#222;margin-top:4px}
.area.featured h3{color:var(--orange)}
.area p{font-size:13px;line-height:1.6;color:#444;width:205px;margin:14px auto 0}
.area .arrow{margin-top:10px;width:30px;height:14px;stroke:#333;fill:none;stroke-width:1.6}
.area.featured .arrow{stroke:var(--orange)}

/* mission */
.mission{height:482px}
.mission .lead{position:absolute;left:0;top:135px;width:1200px;text-align:center;font-size:21px;line-height:1.55;color:#555;font-weight:300}
.hl-teal{color:var(--teal);font-weight:400}
.hl-orange{color:var(--orange);font-weight:400}

/* testimonials */
.reviews{height:570px;background:linear-gradient(180deg,#5d7c86 0%,#3f555d 55%,#23313a 100%)}
.reviews h4{position:absolute;top:88px;left:0;width:1200px;text-align:center;color:#fff;font-size:20px;font-weight:500}
.review-card{position:absolute;left:211px;top:138px;width:778px;height:296px;background:#fff}
.quote-mark{position:absolute;left:38px;top:30px;width:70px;height:60px;fill:#7fbfc6}
.review-card h5{position:absolute;left:133px;top:34px;width:600px;font-size:24px;line-height:1.45;color:var(--teal);font-weight:500}
.review-card p{position:absolute;left:133px;top:114px;width:610px;font-size:12px;line-height:2;color:#666}
.avatar{position:absolute;left:133px;top:206px;width:56px;height:56px;border-radius:50%;background:linear-gradient(135deg,#d8b08a,#8a5c3e)}
.reviewer{position:absolute;left:206px;top:210px;font-size:19px;color:#333}
.role{position:absolute;left:206px;top:240px;font-size:12px;color:#777}

/* blog */
.blog{height:713px}
.blog h4{position:absolute;left:111px;top:85px;font-size:20px;color:var(--orange);font-weight:500}
.post{position:absolute;top:133px;width:310px}
.post .thumb{width:310px;height:220px}
.post .date{font-size:13px;color:#666;margin-top:16px}
.post h3{font-size:21px;line-height:1.4;font-weight:700;color:#444;margin-top:12px}
.post p{font-size:12px;line-height:2;color:#666;margin-top:12px}
.post svg{width:40px;height:18px;stroke:#222;fill:none;stroke-width:2;margin-top:24px}

/* footer */
.site-footer{height:450px;background:var(--teal)}
.foot-logo{position:absolute;left:112px;top:76px;width:355px;height:105px;background:#fff;display:flex;align-items:center;justify-content:center}
.foot-h{position:absolute;color:#fff;font-size:16px;font-weight:500}
.foot-h::after{content:"";display:block;width:30px;height:1px;background:rgba(255,255,255,.6);margin-top:10px}
.foot-t{position:absolute;color:#fff;font-size:13px;line-height:1.65}
.newsletter{position:absolute;left:112px;top:373px;width:376px;height:42px;display:flex}
.newsletter .in{flex:1;background:rgba(255,255,255,.12);color:rgba(255,255,255,.7);font-size:12px;padding:14px 22px}
.newsletter .go{width:120px;background:var(--orange);color:#fff;font-size:14px;display:flex;align-items:center;justify-content:center}
.ci{position:absolute;left:582px;width:40px;height:40px;border-radius:50%;background:var(--orange);display:flex;align-items:center;justify-content:center}
.ci svg{width:20px;height:20px;fill:#fff}
.ct{position:absolute;left:636px;color:#fff;font-size:15px;line-height:1.65}
.social{position:absolute;left:911px;top:160px;display:flex;gap:11px}
.social i{display:block;width:26px;height:26px;border-radius:50%;background:#fff}
.copyline{position:absolute;left:0;top:4165px;width:1200px;height:78px;background:var(--sky);font-size:12px;color:#333;display:flex;align-items:center;justify-content:center}
</style>
</head>
<body>

<header class="site-header">
  <div class="brand abs" style="left:111px;top:30px"><span class="brand-mark"></span>Morillaqua Corvell</div>
  <nav class="nav">
    <a class="active">Home</a><a>About Us</a><a>Our services</a><a>Contact Us</a>
  </nav>
  <div class="btn" style="left:836px;top:26px;width:120px;height:40px">Download</div>
  <div class="lang"><span class="flag"></span>English ⌄</div>
</header>

<section class="hero">
  <div class="hero-desk" role="img" aria-label="Soft blurred office desk and city skyline in the background"></div>
  <div class="hero-portrait" role="img" aria-label="Smiling lawyer in glasses blended with a city skyline"></div>
  <div class="hero-text">
    <div class="pre">Broad Range of</div>
    <h1>Legal Services</h1>
    <div class="sub">in Australia and overseas.</div>
    <p>Our small, skilled team is committed to the delivery of<br>quality legal services to our clients.</p>
  </div>
  <div class="btn" style="left:267px;top:403px;width:120px;height:40px">Contact Us</div>
  <div class="dots" style="left:301px;top:534px"><i class="on"></i><i></i><i></i><i></i></div>
  <div class="quick">Quick Enquiry Now</div>
</section>

<section class="welcome">
  <div class="pre">Welcome to</div>
  <h2>Morillaqua Corvell</h2>
  <div class="copy">
    Morillaqua Corvell is a successor to the legal practice founded by Mr Lucien Armand Morillaqua in the 1930?s. Its various transformations saw Mr Lucien Armand Morillaqua and his sons work in partnership with other lawyers prior to forming a smaller family firm (Morillaqua &amp; Morillaqua) on their own.<br><br>
    The firm name was changed to ?Morillaqua? when Henri Morillaqua became sole proprietor of the firm in the early 1990?s.
  </div>
  <div class="outline-btn">LEARN MORE ABOUT US</div>

  <div class="enquiry-note">For more information about the<br>history of the practice and the Morillaqua?</div>
  <div class="field" style="top:73px">Name<svg viewBox="0 0 16 16"><circle cx="8" cy="5" r="3"/><path d="M2 15c0-4 12-4 12 0"/></svg></div>
  <div class="field" style="top:128px">Phone<svg viewBox="0 0 16 16"><path d="M3 2l3 1 1 3-2 1c1 2 2 3 4 4l1-2 3 1 1 3c-6 1-12-5-11-11z"/></svg></div>
  <div class="field" style="top:183px">Email<svg viewBox="0 0 16 16"><rect x="1.5" y="3.5" width="13" height="9"/><path d="M1.5 3.5l6.5 5 6.5-5"/></svg></div>
  <div class="field" style="top:238px;height:106px">Message<svg viewBox="0 0 16 16"><path d="M2 3h12v8H7l-3 3v-3H2z"/></svg></div>
  <div class="appt">Make An Appointment<svg viewBox="0 0 16 16" width="14" height="14" fill="none" stroke="#fff" stroke-width="1.5"><path d="M15 1L1 7l5 2 2 6z M6 9l9-8"/></svg></div>
</section>

<section class="practice">
  <div class="scale-deco" role="img" aria-label="Faint scales of justice and gavel in the background"></div>
  <div class="sec-pre" style="top:75px">What We Offer</div>
  <div class="sec-title" style="top:95px">Our Practice Areas</div>

  <div class="area" style="left:87px;top:193px"><svg class="icon" viewBox="0 0 44 44"><rect x="12" y="6" width="20" height="34"/><rect x="4" y="18" width="8" height="22"/><rect x="32" y="18" width="8" height="22"/><path d="M17 12h3M24 12h3M17 19h3M24 19h3M17 26h3M24 26h3M20 40v-7h4v7"/></svg><h3>Property Law</h3><p>Our Property Law team has the legal knowledge and experience to make your purchase or sale of real estate as smooth as possible.</p><svg class="arrow" viewBox="0 0 30 14"><path d="M1 7h27M22 1l6 6-6 6"/></svg></div>

  <div class="area featured" style="left:345px;top:193px"><svg class="icon" viewBox="0 0 44 44"><path d="M4 26l10-9 8 5 14-12"/><circle cx="36" cy="8" r="3"/><ellipse cx="14" cy="34" rx="6" ry="2"/><path d="M8 34v6c0 1 12 1 12 0v-6M24 30v10c0 1 12 1 12 0V30"/><ellipse cx="30" cy="30" rx="6" ry="2"/></svg><h3>Sale of Business</h3><p>Our Property Law team has the legal knowledge and experience to make your purchase or sale of real estate as smooth as possible.</p><svg class="arrow" viewBox="0 0 30 14"><path d="M1 7h27M22 1l6 6-6 6"/></svg></div>

  <div class="area" style="left:601px;top:193px"><svg class="icon" viewBox="0 0 44 44"><circle cx="22" cy="10" r="5"/><path d="M22 15v12M14 21h16M6 30h32v6H6zM10 36v4h24v-4"/></svg><h3>Wills &amp; Estates</h3><p>Our Property Law team has the legal knowledge and experience to make your purchase or sale of real estate as smooth as possible.</p><svg class="arrow" viewBox="0 0 30 14"><path d="M1 7h27M22 1l6 6-6 6"/></svg></div>

  <div class="area" style="left:858px;top:193px"><svg class="icon" viewBox="0 0 44 44"><circle cx="22" cy="18" r="13"/><path d="M9 18h26M22 5c-6 7-6 19 0 26M22 5c6 7 6 19 0 26M12 34l-4 6h28l-4-6"/></svg><h3>Translation</h3><p>Our Property Law team has the legal knowledge and experience to make your purchase or sale of real estate as smooth as possible.</p><svg class="arrow" viewBox="0 0 30 14"><path d="M1 7h27M22 1l6 6-6 6"/></svg></div>

  <div class="area" style="left:87px;top:475px"><svg class="icon" viewBox="0 0 44 44"><circle cx="16" cy="8" r="4"/><circle cx="30" cy="10" r="4"/><path d="M12 16h8l2 12h-12zM26 18h8l1 10h-10M14 28v12M18 28v12M28 28v12M32 28v12M6 22l-2 18"/></svg><h3>Elder Law</h3><p>Our Property Law team has the legal knowledge and experience to make your purchase or sale of real estate as smooth as possible.</p><svg class="arrow" viewBox="0 0 30 14"><path d="M1 7h27M22 1l6 6-6 6"/></svg></div>

  <div class="area" style="left:345px;top:475px"><svg class="icon" viewBox="0 0 44 44"><path d="M22 4v34M8 10h28M8 10l-6 14h12zM36 10l-6 14h12zM14 40h16"/></svg><h3>Powers of Attorney</h3><p>Our Property Law team has the legal knowledge and experience to make your purchase or sale of real estate as smooth as possible.</p><svg class="arrow" viewBox="0 0 30 14"><path d="M1 7h27M22 1l6 6-6 6"/></svg></div>

  <div class="area" style="left:601px;top:475px"><svg class="icon" viewBox="0 0 44 44"><ellipse cx="26" cy="12" rx="12" ry="8"/><path d="M21 12h2M26 12h2M4 28h8l8 4h10l8-6v4l-10 8H12l-8-2z"/></svg><h3>French advice</h3><p>Our Property Law team has the legal knowledge and experience to make your purchase or sale of real estate as smooth as possible.</p><svg class="arrow" viewBox="0 0 30 14"><path d="M1 7h27M22 1l6 6-6 6"/></svg></div>

  <div class="area" style="left:858px;top:475px"><svg class="icon" viewBox="0 0 44 44"><circle cx="10" cy="8" r="4"/><circle cx="22" cy="6" r="4"/><circle cx="34" cy="8" r="4"/><path d="M4 22c0-6 12-6 12 0M28 22c0-6 12-6 12 0M16 18c0-6 12-6 12 0M6 28h32M10 28l-4 12M34 28l4 12"/></svg><h3>Affairs management</h3><p>Our Property Law team has the legal knowledge and experience to make your purchase or sale of real estate as smooth as possible.</p><svg class="arrow" viewBox="0 0 30 14"><path d="M1 7h27M22 1l6 6-6 6"/></svg></div>
</section>

<section class="mission">
  <div class="sec-pre" style="top:65px">Morillaqua Corvell</div>
  <div class="sec-title" style="top:82px">Mission statement</div>
  <div class="lead">
    Morillaqua Corvell is a successor to the legal practice founded by<br>
    <span class="hl-teal">Mr Lucien Armand Morillaqua</span> in the 1930?s.<br><br>
    Its various transformations saw <span class="hl-orange">Mr Lucien Armand</span><br>
    Morillaqua and his sons work in partnership with other lawyers prior to forming<br>
    a smaller family firm (Morillaqua &amp; Morillaqua) on their own.
  </div>
  <div class="btn" style="left:540px;top:370px;width:120px;height:40px">Contact Us</div>
</section>

<section class="reviews" role="img" aria-label="Dark background of a gavel resting on a desk">
  <h4>Our Happy Customers Says</h4>
  <div class="review-card">
    <svg class="quote-mark" viewBox="0 0 70 60"><path d="M2 58V32C2 14 10 6 28 2l2 8C20 13 16 20 16 28h14v30zM40 58V32c0-18 8-26 26-30l2 8c-10 3-14 10-14 18h14v30z"/></svg>
    <h5>Morillaqua Corvell Lorem ipsum dolor sit amet, consectetur adipiscing.</h5>
    <p>Lorem ipsum dolor sit amet, consectetur adipiscing elit, sed do eiusmod tempor incididunt ut labore et dolore magna aliqua. Ut enim ad minim veniam, quis nostrud exercitation ullamco laboris nisi ut aliquip ex ea commodo consequat.</p>
    <div class="avatar" role="img" aria-label="Client portrait"></div>
    <div class="reviewer">Margot L. Devereux</div>
    <div class="role">Pro Property Maintenance</div>
  </div>
  <div class="dots" style="left:566px;top:472px"><i style="background:#fff"></i><i></i><i></i><i></i></div>
</section>

<section class="blog">
  <h4>Recent Blog and News</h4>
  <article class="post" style="left:111px">
    <div class="thumb" role="img" aria-label="Couple reviewing a house model with an adviser" style="background:linear-gradient(135deg,#5a4e48,#b9a697 55%,#3b3431)"></div>
    <div class="date">05 April 2024</div>
    <h3>Lorem ipsum is placeholder text commonly the graphic, print.</h3>
    <p>Lorem ipsum dolor sit amet, consectetur adipi-scing elit, sed do eiusmod tempor incididunt ut labore et dolore magna aliqua.</p>
    <svg viewBox="0 0 40 18"><path d="M1 9h36M30 2l7 7-7 7"/></svg>
  </article>
  <article class="post" style="left:444px">
    <div class="thumb" role="img" aria-label="Hands signing a document at a white desk" style="background:linear-gradient(135deg,#2b2f36,#d9dde0 50%,#f2f2f2)"></div>
    <div class="date">03 April 2024</div>
    <h3>Lorem ipsum is placeholder text commonly the graphic, print.</h3>
    <p>Lorem ipsum dolor sit amet, consectetur adipi-scing elit, sed do eiusmod tempor incididunt ut labore et dolore magna aliqua.</p>
    <svg viewBox="0 0 40 18"><path d="M1 9h36M30 2l7 7-7 7"/></svg>
  </article>
  <article class="post" style="left:777px">
    <div class="thumb" role="img" aria-label="Woman holding a tablet surrounded by greetings in many languages" style="background:linear-gradient(135deg,#eef0f3,#e6a36c 50%,#eef0f3)"></div>
    <div class="date">02 April 2024</div>
    <h3>Lorem ipsum is placeholder text commonly the graphic, print.</h3>
    <p>Lorem ipsum dolor sit amet, consectetur adipi-scing elit, sed do eiusmod tempor incididunt ut labore et dolore magna aliqua.</p>
    <svg viewBox="0 0 40 18"><path d="M1 9h36M30 2l7 7-7 7"/></svg>
  </article>
</section>

<footer class="site-footer">
  <div class="foot-logo"><div class="brand"><span class="brand-mark"></span>Morillaqua Corvell</div></div>
  <div class="foot-h" style="left:112px;top:228px">Subscribe Our Newsletter</div>
  <div class="foot-t" style="left:112px;top:282px;width:340px;font-size:12.5px">All of our services are available in English or in French according to the needs of our clients.</div>
  <div class="newsletter"><div class="in">Email Address</div><div class="go">Subscriber</div></div>

  <div class="foot-h" style="left:580px;top:85px">Contact Us:</div>
  <div class="ci" style="top:143px"><svg viewBox="0 0 20 20"><path d="M10 1a6 6 0 016 6c0 5-6 12-6 12S4 12 4 7a6 6 0 016-6zm0 4a2 2 0 100 4 2 2 0 000-4z"/></svg></div>
  <div class="ct" style="top:145px;font-weight:500">Level 9, 48 Harbour Lane<br>Sydney, NSW 2000 Australia</div>
  <div class="ci" style="top:233px"><svg viewBox="0 0 20 20"><path d="M4 2l4 1 1 4-2 1c1 2 3 4 5 5l1-2 4 1 1 4c-8 1-16-7-14-14z"/></svg></div>
  <div class="ct" style="top:235px">Call toll free:<br>(+612) 5550 1942</div>
  <div class="ci" style="top:305px"><svg viewBox="0 0 20 20"><path d="M2 5h16v10H2zm1 1l7 5 7-5" stroke="#f5a06e" stroke-width="1"/></svg></div>
  <div class="ct" style="top:305px">Email:<br>clara@corvell.com.au</div>

  <div class="foot-h" style="left:911px;top:85px">Follow Us:</div>
  <div class="social">
    <i role="img" aria-label="Social network link"></i>
    <i role="img" aria-label="Social network link"></i>
    <i role="img" aria-label="Social network link"></i>
    <i role="img" aria-label="Social network link"></i>
    <i role="img" aria-label="Video channel link"></i>
  </div>
  <div class="foot-h" style="left:911px;top:213px">Site Map</div>
  <div class="foot-t" style="left:911px;top:260px;line-height:2">Home<br>About Us<br>Our services<br>Contact Us</div>
</footer>

<div class="copyline">Morillaqua Corvell. © 2024 All Rights Reserved | Privacy Policy | Terms and Conditions</div>

</body>
</html>
```